Heron Creek Lodge Sign

need a physical sign designed for the ranch entry gate. Gate entry picture provided. Could provide drawings if necessary. I have sent a logo and would like to try to use it in this sign design but am open to new or different ideas..

Target Market(s)

upscale out of town/area/country guests. This is a very secluded, high end retreat that offers outdoor activities (shooting for one) in addition to luxury accomodations.

Industry/Entity Type

hospitality

Requirements
Nice to have
• some or all of existing logo

```html
<!DOCTYPE html>
<html lang="en">
<head>
<meta charset="utf-8">
<title>Heron Creek Lodge – Gate Sign</title>
<link href="https://fonts.googleapis.com/css2?family=Lobster&family=Lobster+Two:wght@700&display=swap" rel="stylesheet">
<style>
  :root {
    --sign-red: #e0202b;
    --sign-black: #141414;
    --sign-white: #ffffff;
    --page-bg: #efefef;
  }
  * { margin: 0; padding: 0; box-sizing: border-box; }
  html, body {
    width: 1200px;
    height: 1200px;
    overflow: hidden;
    background: var(--page-bg);
  }
  .gate-sign {
    position: absolute;
    left: 30px;
    top: 314px;
    width: 1140px;
    height: 571px;
    background: var(--sign-white);
    overflow: hidden;
  }
  .sign-curves {
    position: absolute;
    inset: 0;
    width: 100%;
    height: 100%;
  }
  .brand {
    position: absolute;
    left: 58px;
    top: 170px;
    display: flex;
    align-items: center;
    gap: 16px;
  }
  .brand-dot {
    width: 62px;
    height: 62px;
    border-radius: 50%;
    background: var(--sign-red);
    flex: none;
  }
  .brand-name {
    font-family: "Lobster", cursive;
    font-size: 40px;
    font-weight: 400;
    color: var(--sign-black);
    white-space: nowrap;
  }
  .offer {
    position: absolute;
    right: 94px;
    top: 168px;
    text-align: right;
  }
  .offer-line { display: block; white-space: nowrap; }
  .offer-headline {
    font-family: "Lobster", cursive;
    color: var(--sign-red);
    font-size: 52px;
    line-height: 66px;
  }
  .offer-detail {
    font-family: "Lobster Two", cursive;
    font-weight: 700;
    color: var(--sign-black);
    font-size: 42px;
    line-height: 64px;
  }
  .offer-feature {
    font-family: "Lobster", cursive;
    color: var(--sign-red);
    font-size: 80px;
    line-height: 84px;
  }
</style>
</head>
<body>
  <main class="gate-sign">
    <svg class="sign-curves" viewBox="0 0 822 412" preserveAspectRatio="none" aria-hidden="true">
      <path fill="var(--sign-black)" d="M418 0 H610 C560 12 530 30 505 44 C475 32 448 16 418 0 Z"/>
      <path fill="var(--sign-red)" d="M440 0 H822 V88 C720 86 620 80 560 62 C510 48 478 26 440 0 Z"/>
      <path fill="var(--sign-red)" d="M285 412 C400 402 560 396 680 390 C760 384 800 332 822 285 V412 Z"/>
    </svg>

    <div class="brand">
      <span class="brand-dot"></span>
      <span class="brand-name">Heron Creek Lodge</span>
    </div>

    <p class="offer">
      <span class="offer-line offer-headline">Outdoor Activities</span>
      <span class="offer-line offer-detail">(shooting for one)</span>
      <span class="offer-line offer-detail">in addition to</span>
      <span class="offer-line offer-feature">Luxury accomodations</span>
    </p>
  </main>
</body>
</html>
```